App Design for Restaurant App

We need a design for the new Mobile App for the Restaurant Velmo. See attachment for presentation sketches.
There are two attached files: File 2 shows the App in general and File 1 shows the five screens which need to be designed. Your work should contain the general color scheme, icons and layout proposal.
Updates
Hi Designers
There where several questions about the scope of the work. We are looking for a design for an App. The promotion website of the restaurant Velmo can be found under www.restaurant-velmo.example
There you will get an impression of the Corporate Identity used by the restaurant and you will also find the logo.
In the sketch there are several screens which don't need a design, e.g. the cover flow or video screen
please ask if you have any question
kind regards
Tobias
Industry/Entity Type
Restaurant
Look and feel
Each slider illustrates characteristics of the customer's brand and the style your logo design should communicate.

```html
<!DOCTYPE html>
<html lang="de">
<head>
<meta charset="utf-8">
<title>Restaurant Velmo – App Screens</title>
<link rel="stylesheet" href="https://fonts.googleapis.com/css2?family=Source+Sans+3:wght@400;500&display=swap">
<style>
  :root {
    --page: #ffffff;
    --cream: #f8f6c8;
    --olive: #424d1f;
    --olive-dark: #353f16;
    --white: #ffffff;
    --frame: #1a1a1a;
    --photo-top: #c9cfc0;
    --photo-mid: #efe7dc;
    --photo-low: #a5704a;
  }
  * { box-sizing: border-box; margin: 0; padding: 0; }
  html, body { width: 1200px; height: 900px; overflow: hidden; background: var(--page); }
  body { position: relative; font-family: "Source Sans 3", "Myriad Pro", sans-serif; color: var(--olive); }

  .screen {
    position: absolute; top: 76px; width: 487px; height: 728px;
    background: var(--cream); border: 1px solid var(--frame);
  }
  .screen--home { left: 72px; }
  .screen--restaurant { left: 642px; }

  .app-header {
    position: absolute; left: 48px; width: 391px; height: 120px; background: var(--white);
  }
  .screen--home .app-header { top: 19px; }
  .screen--restaurant .app-header { top: 22px; left: 46px; }
  .brand-name {
    position: absolute; left: 0; right: 0; top: 70px; text-align: center;
    font-size: 31px; font-weight: 400; letter-spacing: 0.2px; color: var(--olive);
  }
  .brand-dot {
    position: absolute; left: 50%; top: 18px; width: 36px; height: 36px; margin-left: -18px;
    border-radius: 50%; background: var(--olive);
  }
  .menu-grid-icon {
    position: absolute; right: 7px; top: 36px; width: 48px; height: 47px;
  }

  .photo-frame {
    position: absolute; left: 16px; width: 455px; height: 147px; background: var(--white);
  }
  .screen--home .photo-frame { top: 159px; }
  .screen--restaurant .photo-frame { top: 164px; }
  .photo {
    position: absolute; left: 2px; right: 2px; top: 8px; bottom: 7px;
    background: linear-gradient(180deg, var(--photo-top) 0%, var(--photo-mid) 35%, #f4f1ea 60%, var(--photo-low) 100%);
  }

  .nav-panel {
    position: absolute; left: 48px; top: 366px; width: 391px; height: 331px;
    background: var(--white); box-shadow: 6px 6px 0 var(--olive-dark);
    display: grid; grid-template-columns: repeat(3, 1fr); grid-template-rows: repeat(3, 1fr);
    padding: 14px 0 20px;
  }
  .nav-item {
    display: flex; flex-direction: column; align-items: center; justify-content: center; gap: 10px;
    font-size: 19px; color: var(--olive);
  }
  .nav-item svg { width: 48px; height: 40px; }

  .back-tab {
    position: absolute; left: -1px; top: 59px; width: 103px; height: 37px;
  }
  .back-tab span {
    position: absolute; left: 30px; top: 5px; font-size: 19px; color: var(--white);
  }

  .page-links { position: absolute; left: 48px; top: 374px; width: 398px; }
  .page-link {
    display: block; width: 393px; height: 38px; margin-bottom: 36px;
    background: var(--white); box-shadow: 5px 5px 0 var(--olive-dark);
    text-align: center; line-height: 38px; font-size: 19px; color: var(--olive);
  }
</style>
</head>
<body>

<section class="screen screen--home">
  <header class="app-header">
    <div class="brand-dot"></div>
    <div class="brand-name">RESTAURANT VELMO</div>
    <svg class="menu-grid-icon" viewBox="0 0 48 47" aria-hidden="true">
      <rect x="0" y="0" width="21" height="20" fill="#424d1f"/><rect x="27" y="0" width="21" height="20" fill="#424d1f"/>
      <rect x="0" y="27" width="21" height="20" fill="#424d1f"/><rect x="27" y="27" width="21" height="20" fill="#424d1f"/>
    </svg>
  </header>
  <div class="photo-frame"><div class="photo" role="img" aria-label="Festlich gedeckter Speisesaal mit weissen Tischen und Panoramafenstern"></div></div>

  <nav class="nav-panel">
    <div class="nav-item">
      <svg viewBox="0 0 48 40"><circle cx="24" cy="20" r="18" fill="#424d1f"/><circle cx="24" cy="11" r="3" fill="#f8f6c8"/><path d="M21 16h5v11h3v3H18v-3h3z" fill="#f8f6c8"/></svg>
      Aktuell</div>
    <div class="nav-item">
      <svg viewBox="0 0 48 40"><rect x="2" y="10" width="32" height="20" rx="2" fill="#424d1f"/><path d="M34 17l12-6v18l-12-6z" fill="#424d1f"/></svg>
      Webcam</div>
    <div class="nav-item">
      <svg viewBox="0 0 48 40"><path d="M24 2L2 22h8v16h28V22h8z" fill="#424d1f"/></svg>
      Restaurant</div>
    <div class="nav-item">
      <svg viewBox="0 0 48 40"><path d="M18 2l14 14-5 2-4 10-11-11 10-4z" fill="#424d1f"/><path d="M15 22L6 38l2 1 12-13z" fill="#424d1f"/></svg>
      Events</div>
    <div class="nav-item">
      <svg viewBox="0 0 48 40"><rect x="4" y="1" width="40" height="38" fill="#424d1f"/><g fill="#8a9367"><rect x="7" y="12" width="34" height="1.5"/><rect x="7" y="19" width="34" height="1.5"/><rect x="7" y="26" width="34" height="1.5"/><rect x="7" y="33" width="34" height="1.5"/><rect x="13" y="10" width="1.5" height="27"/><rect x="20" y="10" width="1.5" height="27"/><rect x="27" y="10" width="1.5" height="27"/><rect x="34" y="10" width="1.5" height="27"/></g></svg>
      Reservations</div>
    <div class="nav-item">
      <svg viewBox="0 0 48 40"><g fill="#424d1f"><path d="M2 6q22-4 44 0v4q-22-4-44 0z"/><path d="M2 15q22-4 44 0v4q-22-4-44 0z"/><path d="M2 24q22-4 44 0v4q-22-4-44 0z"/><path d="M2 33q22-4 44 0v4q-22-4-44 0z"/></g></svg>
      Menükarte</div>
    <div class="nav-item">
      <svg viewBox="0 0 48 40"><rect x="2" y="6" width="44" height="30" rx="2" fill="#424d1f"/><circle cx="24" cy="21" r="8" fill="none" stroke="#8a9367" stroke-width="2"/><rect x="6" y="9" width="8" height="3" fill="#8a9367"/></svg>
      Galerie</div>
    <div class="nav-item">
      <svg viewBox="0 0 48 40"><path d="M36 4L12 24l10 1 3 11z" fill="#424d1f"/></svg>
      Anfahrt</div>
    <div class="nav-item">
      <svg viewBox="0 0 48 40"><path d="M2 8q11-4 21 1v28q-10-5-21-1z" fill="#424d1f"/><path d="M46 8q-11-4-21 1v28q10-5 21-1z" fill="#424d1f"/></svg>
      Gästebuch</div>
  </nav>
</section>

<section class="screen screen--restaurant">
  <header class="app-header">
    <div class="brand-dot"></div>
    <div class="brand-name">RESTAURANT VELMO</div>
    <svg class="menu-grid-icon" viewBox="0 0 48 47" aria-hidden="true">
      <rect x="0" y="0" width="21" height="20" fill="#424d1f"/><rect x="27" y="0" width="21" height="20" fill="#424d1f"/>
      <rect x="0" y="27" width="21" height="20" fill="#424d1f"/><rect x="27" y="27" width="21" height="20" fill="#424d1f"/>
    </svg>
  </header>
  <div class="back-tab">
    <svg viewBox="0 0 103 37" width="103" height="37" aria-hidden="true"><path d="M0 18.5L24 0h79v37H24z" fill="#424d1f"/></svg>
    <span>Zurück</span>
  </div>
  <div class="photo-frame"><div class="photo" role="img" aria-label="Festlich gedeckter Speisesaal mit weissen Tischen und Panoramafenstern"></div></div>

  <nav class="page-links">
    <a class="page-link">Wir stellen uns vor...</a>
    <a class="page-link">Das Team</a>
    <a class="page-link">Öffnungszeiten</a>
    <a class="page-link">Kontakt</a>
  </nav>
</section>

</body>
</html>
```